Eastfield Commercial Card

I would like a modern, eye catching card based off my logo design.
Info to include:
Anders Voll (Card Name)
eastfieldcommercial.example (Website)
555 203 8841 (Office/fax)
555 287 3096 (Business Cell)
anders@eastfieldcommercial.example (Work email)

Target Market(s)

Commercial real estate brokers, property owners.

Colors
ec1f27
757575

Requirements
Must have
• Name and info above. Not be lame!:)

```html
<!DOCTYPE html>
<html lang="en">
<head>
<meta charset="utf-8">
<title>Eastfield Commercial – Business Card</title>
<link rel="stylesheet" href="https://fonts.googleapis.com/css2?family=Montserrat:wght@400;500;700&display=swap">
<style>
  :root {
    --brand-red: #ec1f27;
    --card-red: #f20d13;
    --brand-grey: #757575;
    --ink-dark: #2d2d30;
    --card-black: #12131a;
    --backdrop-top: #5b6066;
    --backdrop-bottom: #1f2225;
    --white: #ffffff;
  }
  * { box-sizing: border-box; margin: 0; padding: 0; }
  html, body { width: 1200px; height: 1200px; overflow: hidden; }
  body {
    font-family: "Montserrat", sans-serif;
    background: radial-gradient(ellipse at 50% 30%, var(--backdrop-top), var(--backdrop-bottom) 75%);
    position: relative;
  }
  .card {
    position: absolute;
    left: 220px;
    width: 760px;
    height: 434px;
    box-shadow: 0 14px 30px rgba(0,0,0,0.45);
  }
  .card--front { top: 130px; background: var(--card-black); }
  .card--back { top: 636px; background: var(--card-red); }

  .brand {
    position: absolute;
    left: 0; right: 0;
    display: flex;
    align-items: center;
    justify-content: center;
    gap: 14px;
  }
  .brand__mark { width: 22px; height: 22px; }
  .brand__name { font-weight: 700; text-transform: uppercase; letter-spacing: 0.5px; }

  .card--front .brand { top: 170px; }
  .card--front .brand__mark { background: var(--brand-grey); }
  .card--front .brand__name { color: var(--brand-red); font-size: 36px; }
  .front__web {
    position: absolute;
    top: 300px; left: 0; right: 0;
    text-align: center;
    color: #8a1418;
    font-size: 18px;
    letter-spacing: 0.5px;
  }

  .card--back .brand { top: 70px; }
  .card--back .brand__mark { background: var(--ink-dark); }
  .card--back .brand__name { color: var(--ink-dark); font-size: 28px; }

  .holder {
    position: absolute;
    left: 30px; top: 230px;
    width: 290px;
    text-align: right;
  }
  .holder__name { font-size: 42px; font-weight: 500; color: var(--ink-dark); line-height: 1.1; }
  .holder__role { font-size: 20px; color: var(--white); margin-top: 4px; }

  .divider {
    position: absolute;
    left: 340px; top: 190px;
    width: 2px; height: 190px;
    background: var(--white);
  }

  .contacts {
    position: absolute;
    left: 362px; top: 196px;
    list-style: none;
  }
  .contacts__item {
    display: flex;
    align-items: center;
    gap: 12px;
    height: 46px;
    font-size: 17px;
    color: var(--ink-dark);
    font-weight: 500;
  }
  .contacts__icon { width: 24px; height: 24px; flex: none; }
</style>
</head>
<body>

<section class="card card--front" aria-label="Card front">
  <div class="brand">
    <span class="brand__mark"></span>
    <span class="brand__name">Eastfield Commercial</span>
  </div>
  <p class="front__web">www.eastfieldcommercial.example</p>
</section>

<section class="card card--back" aria-label="Card back">
  <div class="brand">
    <span class="brand__mark"></span>
    <span class="brand__name">Eastfield Commercial</span>
  </div>

  <div class="holder">
    <p class="holder__name">Anders Voll</p>
    <p class="holder__role">CEO</p>
  </div>

  <div class="divider"></div>

  <ul class="contacts">
    <li class="contacts__item">
      <svg class="contacts__icon" viewBox="0 0 24 24" fill="none" stroke="#fff" stroke-width="2" stroke-linecap="round" stroke-linejoin="round"><path d="M5 3h4l2 5-2.5 1.5a11 11 0 0 0 6 6L16 13l5 2v4a2 2 0 0 1-2 2A16 16 0 0 1 3 5a2 2 0 0 1 2-2z"/></svg>
      <span>555 287 3096</span>
    </li>
    <li class="contacts__item">
      <svg class="contacts__icon" viewBox="0 0 24 24" fill="#fff"><rect x="6" y="2" width="12" height="6"/><rect x="2" y="9" width="20" height="9" rx="2"/><rect x="6" y="15" width="12" height="7" fill="#fff" stroke="#f20d13" stroke-width="1.5"/></svg>
      <span>555 203 8841</span>
    </li>
    <li class="contacts__item">
      <svg class="contacts__icon" viewBox="0 0 24 24" fill="none" stroke="#fff" stroke-width="2"><circle cx="12" cy="12" r="10"/><ellipse cx="12" cy="12" rx="4" ry="10"/><path d="M2 12h20M4 7h16M4 17h16"/></svg>
      <span>eastfieldcommercial.example</span>
    </li>
    <li class="contacts__item">
      <svg class="contacts__icon" viewBox="0 0 24 24" fill="#fff"><path d="M2 6h20v13H2z"/><path d="M2 6l10 7 10-7" fill="none" stroke="#f20d13" stroke-width="1.6"/></svg>
      <span>anders@eastfieldcommercial.example</span>
    </li>
  </ul>
</section>

</body>
</html>
```